Flyer for Custom Home Builder!

my company is Harlow Ridge Homes, I am looking for a flyer that we can send via email to a customer, or print and hand out. I am thinking four pages so we could print this and fold it., possibly creating a folder. The name of the company is Harlow Ridge Homes our website is here www.harlowridgehomes-example.com. Some text you can use "Crafting luxury homes isn't just a job, it's our passion.
With meticulous attention to detail and an unwavering commitment to using the finest materials, Harlow Ridge Homes consistently delivers exceptional results that stand as a testament to our commitment to quality."

"Trust is the cornerstone of our foundation.
With a proven track record of delivering on our promises for over 16 years, we prioritize transparent communication and integrity throughout every step of the home-building journey".

you may need to obtain the photos here
https://files.example-share.net/f/k27pw4m8zrt03xq61bnv/h?key=48vn2c9q1x7mb5t0ekd3h&dl=0

Target Market(s)

We build homes for every wealthy clients, therefore the photos are extremely important

Industry/Entity Type

Construction.

Requirements
Must have
• clear larger photos

```html
<!DOCTYPE html>
<html lang="en">
<head>
<meta charset="utf-8">
<title>Harlow Ridge Homes — Flyer</title>
<link rel="stylesheet" href="https://fonts.googleapis.com/css2?family=Anton&family=Josefin+Sans:wght@400;600&family=Oswald:wght@600&display=swap">
<style>
  :root {
    --backdrop: #ebebeb;
    --paper: #ffffff;
    --charcoal: #3d3d3f;
    --ink: #222222;
    --white: #ffffff;
    --logo-grey: #3a3a3c;
    --hero-top: #8d8f93;
    --hero-mid: #9a9ca0;
    --hero-low: #7a6a58;
  }
  * { margin: 0; padding: 0; box-sizing: border-box; }
  html, body { width: 1200px; height: 1200px; overflow: hidden; }
  body { background: var(--backdrop); position: relative; font-family: "Josefin Sans", sans-serif; }

  .flyer {
    position: absolute; left: 233px; top: 81px;
    width: 733px; height: 1038px;
    background: var(--paper);
    overflow: hidden;
  }

  .hero {
    position: absolute; left: 0; top: 0; width: 733px; height: 510px;
    background:
      linear-gradient(180deg, rgba(60,60,64,0.25) 0%, rgba(40,40,44,0.35) 100%),
      linear-gradient(180deg, var(--hero-top) 0%, var(--hero-mid) 45%, #6b7890 62%, var(--hero-low) 100%);
  }
  .brand {
    position: absolute; left: 0; right: 0; top: 62px;
    text-align: center;
    font-family: "Oswald", sans-serif; font-weight: 600;
    font-size: 40px; letter-spacing: 4px; line-height: 1;
    color: var(--logo-grey);
  }
  .headline {
    position: absolute; left: 0; right: 0; top: 262px;
    text-align: center; color: var(--white);
    font-family: "Anton", sans-serif; font-weight: 400;
    text-transform: uppercase; line-height: 1.02;
    text-shadow: 3px 4px 0 rgba(0,0,0,0.55);
  }
  .headline .line-lg { display: block; font-size: 74px; }
  .headline .line-sm { display: block; font-size: 50px; margin: 4px 0 6px; }

  .divider {
    position: absolute; left: 170px; top: 532px;
    width: 391px; height: 6px; background: var(--charcoal);
  }
  .intro {
    position: absolute; left: 40px; right: 40px; top: 566px;
    text-align: center; color: var(--ink);
    font-size: 19px; line-height: 28px;
  }

  .gallery { position: absolute; left: 0; top: 0; width: 733px; height: 1038px; }

  .website {
    position: absolute; left: 0; top: 982px; width: 298px; height: 34px;
    background: var(--charcoal); color: var(--white);
    display: flex; align-items: center; gap: 10px; padding-left: 34px;
    font-size: 13px; letter-spacing: 0.3px;
  }
  .contact {
    position: absolute; right: 28px; top: 942px;
    list-style: none; color: var(--ink);
    font-size: 13px; line-height: 19px; text-align: right;
  }
  .contact li { display: flex; justify-content: flex-end; align-items: flex-start; gap: 10px; }
  .contact .icon { width: 10px; height: 10px; margin-top: 3px; flex: none; }
  .contact .spacer { width: 10px; flex: none; }
</style>
</head>
<body>
  <main class="flyer">
    <section class="hero" role="img" aria-label="Photo of a bright open-plan living room and kitchen with vaulted white ceiling, navy sofas and cabinets, pendant lights and wide oak floors">
      <div class="brand">HARLOW RIDGE HOMES</div>
      <h1 class="headline">
        <span class="line-lg">Crafting Luxury</span>
        <span class="line-sm">Homes isn't just a job,</span>
        <span class="line-lg">It's our passion</span>
      </h1>
    </section>

    <div class="divider"></div>

    <p class="intro">
      Trust is the cornerstone of our foundation.<br>
      With a proven track record of delivering on our promises for over<br>
      16 years, we prioritize transparent communication and integrity<br>
      throughout every step of the home-building journey
    </p>

    <svg class="gallery" viewBox="0 0 733 1038" xmlns="http://www.w3.org/2000/svg">
      <defs>
        <linearGradient id="dusk-facade" x1="0" y1="0" x2="0" y2="1">
          <stop offset="0" stop-color="#2e4a78"/>
          <stop offset="0.45" stop-color="#7d86a0"/>
          <stop offset="0.6" stop-color="#c79a78"/>
          <stop offset="1" stop-color="#6e6a66"/>
        </linearGradient>
        <linearGradient id="pool-terrace" x1="0" y1="0" x2="0" y2="1">
          <stop offset="0" stop-color="#8fb7da"/>
          <stop offset="0.45" stop-color="#cfc9c0"/>
          <stop offset="0.7" stop-color="#4fb6c6"/>
          <stop offset="1" stop-color="#9a9590"/>
        </linearGradient>
      </defs>
      <rect class="connector" x="335" y="769" width="69" height="62" fill="var(--charcoal)"/>
      <polygon role="img" aria-label="Photo of a white multi-storey coastal home with wraparound balconies at dusk"
        points="94,709 348,709 324,903 70,903" fill="url(#dusk-facade)" stroke="var(--charcoal)" stroke-width="5"/>
      <polygon role="img" aria-label="Photo of a modern home with covered terrace beside a turquoise pool and spa"
        points="408,709 663,709 639,903 384,903" fill="url(#pool-terrace)" stroke="var(--charcoal)" stroke-width="5"/>
    </svg>

    <ul class="contact">
      <li>555-014-2290
        <svg class="icon" viewBox="0 0 10 10"><path d="M2 1 L4 1 L4.6 3 L3.4 4 Q4.5 6 6 6.6 L7 5.4 L9 6 L9 8 Q8 9 6.5 8.6 Q2.5 7 1.2 3.5 Q1 2 2 1 Z" fill="var(--ink)"/></svg>
      </li>
      <li>info@harlowridge-example.com
        <svg class="icon" viewBox="0 0 10 10"><rect x="0.5" y="2" width="9" height="6.5" rx="1" fill="var(--ink)"/><path d="M1 2.6 L5 5.6 L9 2.6" stroke="var(--paper)" stroke-width="0.8" fill="none"/></svg>
      </li>
      <li>480 Larkspur Bend,
        <svg class="icon" viewBox="0 0 10 10"><path d="M5 0.8 A2.8 2.8 0 0 1 7.8 3.6 C7.8 5.6 5 8.6 5 8.6 C5 8.6 2.2 5.6 2.2 3.6 A2.8 2.8 0 0 1 5 0.8 Z" fill="var(--ink)"/><circle cx="5" cy="3.6" r="1" fill="var(--paper)"/></svg>
      </li>
      <li>Suite 210, Cedar Falls TX 78999<span class="spacer"></span></li>
    </ul>

    <div class="website">
      <svg width="11" height="11" viewBox="0 0 12 12" fill="none" stroke="var(--white)" stroke-width="1">
        <circle cx="6" cy="6" r="5"/><ellipse cx="6" cy="6" rx="2.2" ry="5"/><path d="M1 6 H11"/>
      </svg>
      <span>www.harlowridgehomes-example.com</span>
    </div>
  </main>
</body>
</html>
```